Halvorn Hire Business Card Design

Need business cards designed for our new equipment rental. We specialize in renting to landscape / tree professionals, contractors, Do-It-Yourself'ers and Around the home or office. Looking for a eye catching card. Landscape and construction should be the theme. The logo is attached, and you can see our colors from the logo. You can use whatever color goes with it ok.

Target Market(s)

First off Landscape and Tree Professional. Then contractors, Do-It-Yourself'ers and rentals for Around the home or office.

Industry/Entity Type

Business

Contact Information for Business Card

Eye catching background that blends landscaping with construction equipment

Requirements
Must have
• Name on Card will Be: Derek Pollard (Manager)
• My Direct Phone Number is: 352-418-7093
• derek@halvornhire.example
• www.halvornhire.example
• 4172 Wexley Mill Road,
• Dade City FL 33590
Nice to have
• Would be Nice to have these bullets on the Face of the card that does not have all my information.
• Serving:
• Landscape / Tree Professionals
• Contractors
• DYI'ers or say Do-It-Yourself'ers
• Maybe have serving small and centered above these bullets, and these 3 bullets along the bottom of the card. Ideas?

```html
<!DOCTYPE html>
<html lang="en">
<head>
<meta charset="utf-8">
<title>Halvorn Hire Business Card</title>
<link href="https://fonts.googleapis.com/css2?family=Work+Sans:wght@400;500;700&display=swap" rel="stylesheet">
<style>
  :root {
    --backdrop: #2b2b2d;
    --card: #1c1c1e;
    --card-sheen: #26262a;
    --silver: #cfcfd2;
    --gold: #f2b443;
    --text: #ececec;
    --rule: #dcdcdc;
  }
  html, body {
    margin: 0;
    width: 1200px;
    height: 900px;
    overflow: hidden;
    background: var(--backdrop);
    font-family: "Work Sans", Arial, sans-serif;
  }
  .canvas {
    position: relative;
    width: 1200px;
    height: 900px;
  }
  .card {
    position: absolute;
    left: 270px;
    width: 660px;
    height: 377px;
    background: linear-gradient(135deg, var(--card) 0%, var(--card) 55%, var(--card-sheen) 100%);
    box-shadow: 0 12px 32px rgba(0,0,0,.5);
  }
  .card--front { top: 40px; }
  .card--back { top: 475px; }

  .brand {
    position: absolute;
    display: flex;
    align-items: center;
    gap: 14px;
    white-space: nowrap;
  }
  .brand__mark {
    flex: none;
    background: var(--silver);
  }
  .brand__name {
    font-weight: 700;
    color: var(--silver);
    letter-spacing: 2px;
    text-transform: uppercase;
  }
  .card--front .brand {
    left: 0;
    right: 0;
    top: 150px;
    justify-content: center;
  }
  .card--front .brand__mark { width: 40px; height: 40px; }
  .card--front .brand__name { font-size: 52px; }

  .card--back .brand {
    left: 28px;
    top: 165px;
  }
  .card--back .brand__mark { width: 24px; height: 24px; }
  .card--back .brand__name { font-size: 31px; letter-spacing: 1px; }

  .divider {
    position: absolute;
    left: 318px;
    top: 48px;
    width: 2px;
    height: 282px;
    background: var(--rule);
  }
  .contact {
    position: absolute;
    left: 345px;
    top: 54px;
    color: var(--text);
  }
  .contact__name {
    margin: 0;
    font-size: 30px;
    font-weight: 500;
    color: var(--gold);
    letter-spacing: 1px;
    text-transform: uppercase;
  }
  .contact__role {
    margin: 0 0 14px;
    font-size: 18px;
  }
  .contact__address {
    margin: 0 0 12px;
    font-size: 18px;
    line-height: 1.3;
    font-style: normal;
  }
  .contact__list {
    list-style: none;
    margin: 0;
    padding: 0;
    font-size: 19px;
  }
  .contact__list li {
    display: flex;
    align-items: center;
    gap: 10px;
    line-height: 1.4;
  }
  .contact__list svg {
    width: 13px;
    height: 13px;
    flex: none;
  }
  .highlight { color: var(--gold); }
</style>
</head>
<body>
<div class="canvas">
  <section class="card card--front">
    <div class="brand">
      <span class="brand__mark"></span>
      <span class="brand__name">Halvorn Hire</span>
    </div>
  </section>

  <section class="card card--back">
    <div class="brand">
      <span class="brand__mark"></span>
      <span class="brand__name">Halvorn Hire</span>
    </div>
    <div class="divider"></div>
    <div class="contact">
      <h1 class="contact__name">Derek Pollard</h1>
      <p class="contact__role">Manager</p>
      <address class="contact__address">4172 Wexley Mill Road,<br>Dade City FL 33590</address>
      <ul class="contact__list">
        <li>
          <svg viewBox="0 0 12 12" aria-hidden="true"><rect x="3" y="0.5" width="6" height="11" rx="1.2" fill="none" stroke="#f2b443" stroke-width="1.2"/><circle cx="6" cy="9.5" r="0.7" fill="#f2b443"/></svg>
          352-418-7093
        </li>
        <li>
          <svg viewBox="0 0 12 12" aria-hidden="true"><path d="M2.5 1 L4.5 1 L5.3 3.5 L4 4.6 Q5.2 7.2 7.4 8 L8.5 6.7 L11 7.5 L11 9.5 Q10.5 11 9 11 Q2 10 1 3 Q1 1.5 2.5 1Z" fill="#f2b443"/></svg>
          352-418-7094
        </li>
        <li>
          <svg viewBox="0 0 12 12" aria-hidden="true"><rect x="0.8" y="2.5" width="10.4" height="7" fill="none" stroke="#f2b443" stroke-width="1.2"/><path d="M1 3 L6 6.5 L11 3" fill="none" stroke="#f2b443" stroke-width="1.2"/></svg>
          derek@halvornhire.example
        </li>
        <li>
          <svg viewBox="0 0 12 12" aria-hidden="true"><circle cx="6" cy="6" r="5" fill="none" stroke="#f2b443" stroke-width="1.1"/><ellipse cx="6" cy="6" rx="2.2" ry="5" fill="none" stroke="#f2b443" stroke-width="1"/><path d="M1 6 H11" stroke="#f2b443" stroke-width="1"/></svg>
          <span>www.<span class="highlight">halvornhire</span>.example</span>
        </li>
      </ul>
    </div>
  </section>
</div>
</body>
</html>
```